Business Card Design Project

Use newly designed logo and tie into newly designed website
I need a new logo and website layout designed for my partner's business. This is a birthday present. His business is interior painting, wallpapering and design. He also has access to a wide variety of products including carpet, fabrics, furniture, wallpaper, tile, countertops, etc. I have attached some screen shots of his website for reference. He is a one man shop and has a stellar reputation with his customers. He is on-time, very tidy, excellent with animals, and always finishes on time and on budget. There are no restrictions on colors or fonts. The logo needs to work well with the website, business cards and printed materials. The website needs to flow content for device size so it looks just as good on a cell phone or tablet as it does on a desktop computer. Whatever the heck that's called!Thanks. I am looking forward to seeing everyone's ideas.
Target Market(s)
Consumers looking to improve the interior environment of their homes by updating wall paint or paper, flooring (either carpet, tile, or hardwoods), counter tops, window treatments, etc. Clients tend to be more upper middle class and have certain taste levels and expectations. New logo, website and business card should align to meet those levels.
Industry/Entity Type
Cell Phone
Look and feel

```html
<!DOCTYPE html>
<html lang="en">
<head>
<meta charset="utf-8">
<title>Vellano Interior Designs – Business Card</title>
<link rel="stylesheet" href="https://fonts.googleapis.com/css2?family=Cinzel:wght@400;600&family=Dosis:wght@400&display=swap">
<style>
  :root {
    --stage: #3a3a3d;
    --plum: #231a45;
    --paper: #ffffff;
    --ink-light: #f4f2f8;
    --gold: #a8956a;
  }
  * { margin: 0; padding: 0; box-sizing: border-box; }
  html, body {
    width: 1200px; height: 780px; overflow: hidden;
    background: var(--stage);
  }
  .card {
    position: absolute; left: 110px; top: 110px;
    width: 980px; height: 560px;
    background: var(--plum);
    display: flex;
  }
  .card__edge { width: 28px; background: var(--plum); }
  .card__brand {
    width: 432px; background: var(--paper);
    display: flex; flex-direction: column; align-items: center; justify-content: center;
    gap: 22px;
  }
  .brand__square {
    width: 150px; height: 150px; background: var(--plum);
  }
  .brand__name {
    font-family: "Cinzel", serif; font-weight: 600; color: var(--plum);
    text-align: center; line-height: 1;
  }
  .brand__name .brand__main { display: block; font-size: 54px; letter-spacing: 1px; }
  .brand__name .brand__sub { display: block; font-size: 22px; letter-spacing: 1.5px; margin-top: 6px; }
  .card__details {
    flex: 1; position: relative; color: var(--ink-light);
    padding: 60px 62px 0 0; text-align: right;
  }
  .holder-name {
    font-family: "Cinzel", serif; font-weight: 400; font-size: 46px;
    letter-spacing: 2px; color: var(--ink-light);
  }
  .contact-list {
    list-style: none; position: absolute; right: 62px; top: 258px;
    font-family: "Dosis", sans-serif; font-size: 25px; line-height: 38px;
  }
  .contact-list li { display: flex; align-items: center; justify-content: flex-end; gap: 12px; }
  .contact-list svg { width: 22px; height: 22px; flex: none; }
</style>
</head>
<body>
  <article class="card">
    <div class="card__edge"></div>
    <section class="card__brand">
      <div class="brand__square"></div>
      <h1 class="brand__name">
        <span class="brand__main">VELLANO</span>
        <span class="brand__sub">INTERIOR DESIGNS</span>
      </h1>
    </section>
    <section class="card__details">
      <h2 class="holder-name">Dorian Vellano</h2>
      <ul class="contact-list">
        <li>(555) 214-3087
          <svg viewBox="0 0 24 24" fill="none" stroke="currentColor" stroke-width="1.6" aria-hidden="true"><rect x="7" y="2.5" width="10" height="19" rx="2"/><line x1="10.5" y1="18" x2="13.5" y2="18"/></svg>
        </li>
        <li>dorian@vellanodesigns.com
          <svg viewBox="0 0 24 24" fill="none" stroke="currentColor" stroke-width="1.6" aria-hidden="true"><rect x="3" y="6" width="18" height="12"/><polyline points="3,6 12,13 21,6"/></svg>
        </li>
        <li>www.vellanodesigns.com
          <svg viewBox="0 0 24 24" fill="none" stroke="currentColor" stroke-width="1.6" aria-hidden="true"><circle cx="12" cy="12" r="8.5"/><ellipse cx="12" cy="12" rx="3.8" ry="8.5"/><line x1="3.5" y1="12" x2="20.5" y2="12"/></svg>
        </li>
        <li>2418 W Larkspur Ct. Fairhaven, KS 66000
          <svg viewBox="0 0 24 24" aria-hidden="true"><path fill="currentColor" d="M12 2a7 7 0 0 0-7 7c0 5 7 13 7 13s7-8 7-13a7 7 0 0 0-7-7zm0 9.5A2.5 2.5 0 1 1 12 6.5a2.5 2.5 0 0 1 0 5z"/></svg>
        </li>
      </ul>
    </section>
  </article>
</body>
</html>
```